BANNER FOR ONLINE CABINET COMPANY MAIN PAGE

Need 3 different banners for the main page. We are online platform for ordering cabinets, parts etc. online.
Website: trimfit.ca
A place where the banner will be placed: https://view.snapvault.example/qR7TpWzKmB4eX
Banner size: 1344x399 pixels
****Clients should get the main point that they can order everything online through the website.

Industry/Entity Type

online cabinets and parts ordering

Requirements
Must have
• online ordering icons, iphone, laptop, desktop pc - so clients get an idea that this is web based service to order cabinets

```html
<!DOCTYPE html>
<html lang="en">
<head>
<meta charset="utf-8">
<title>Trimfit Main Page Banner</title>
<link href="https://fonts.googleapis.com/css2?family=Archivo:wght@400;600;700;800&family=Arimo:wght@400;700&display=swap" rel="stylesheet">
<style>
  :root {
    --header-bg: #2e3032;
    --header-text: #ffffff;
    --phone-box: #111111;
    --green: #27b34a;
    --band-bg: #e4e5e6;
    --title-ink: #111111;
    --sub-ink: #4a4a4a;
    --page-bg: #ffffff;
    --panel: rgba(104, 106, 84, 0.74);
    --text-light: #ffffff;
    --text-soft: #eeeeee;
    --gold: #b58d28;
    --dot: #cfcfcf;
    --dot-active: #f29a12;
    --faint-blue: #e2ebf4;
    --chat-bg: #2b3647;
    --scroll: #f0f0f0;
  }
  * { box-sizing: border-box; margin: 0; padding: 0; }
  html, body { width: 1200px; height: 545px; overflow: hidden; }
  body { background: var(--page-bg); font-family: "Arimo", Arial, sans-serif; position: relative; }

  .site-header {
    position: absolute; left: 0; top: 0; width: 1191px; height: 31px;
    background: var(--header-bg); color: var(--header-text);
  }
  .brand { position: absolute; left: 26px; top: 8px; font-family: "Archivo", Arial, sans-serif; font-weight: 700; font-size: 12px; }
  .brand-divider { position: absolute; left: 98px; top: 6px; width: 1px; height: 19px; background: #ffffff; }
  .tagline { position: absolute; left: 110px; top: 10px; font-size: 8.5px; }
  .contact-box {
    position: absolute; left: 206px; top: 7px; width: 198px; height: 16px;
    background: var(--phone-box); display: flex; align-items: center; gap: 5px; padding-left: 7px; font-size: 7px;
  }
  .contact-box .hours { margin-left: 9px; }
  .main-nav { position: absolute; top: 0; left: 0; height: 31px; width: 100%; font-size: 7.5px; }
  .main-nav span { position: absolute; top: 11px; }
  .nav-cta {
    position: absolute; left: 720px; top: 9px; width: 62px; height: 13px; border-radius: 7px;
    background: var(--green); font-size: 7.5px; text-align: center; line-height: 13px;
  }
  .nav-icon { position: absolute; top: 8px; }

  .title-band { position: absolute; left: 0; top: 31px; width: 1191px; height: 58px; background: var(--band-bg); text-align: center; }
  .title-band h2 {
    font-family: "Archivo", Arial, sans-serif; font-weight: 800; font-size: 18.5px; letter-spacing: 0.6px;
    color: var(--title-ink); margin-top: 5px; line-height: 20px;
  }
  .title-band p { font-size: 13px; color: var(--sub-ink); margin-top: 4px; line-height: 16px; }

  .banner { position: absolute; left: 0; top: 89px; width: 1191px; height: 356px; overflow: hidden; }
  .banner-photo {
    position: absolute; inset: 0;
    background:
      linear-gradient(180deg, rgba(120,118,122,0) 0%, rgba(120,118,122,0) 45%, rgba(30,30,32,0.55) 60%, rgba(30,30,32,0.6) 100%),
      linear-gradient(90deg, #dedad6 0%, #d3cdc7 28%, #c8c2bc 34%, #8f8c8e 45%, #7d7b80 60%, #9a979a 70%, #7a787d 85%, #6c6b70 100%);
  }
  .offer-panel { position: absolute; left: 113px; top: 32px; width: 478px; height: 291px; background: var(--panel); }
  .offer-title {
    position: absolute; left: 43px; top: 29px; color: var(--text-light);
    font-family: "Archivo", Arial, sans-serif; font-size: 29px; font-weight: 700; line-height: 41px;
    text-shadow: 0 1px 3px rgba(0,0,0,0.25); white-space: nowrap;
  }
  .offer-text { position: absolute; left: 43px; top: 167px; width: 365px; color: var(--text-soft); font-size: 12px; line-height: 18px; }
  .device-label {
    position: absolute; left: 43px; top: 239px; color: var(--text-soft);
    font-family: "Archivo", Arial, sans-serif; font-size: 9.3px; font-weight: 600; letter-spacing: 2.3px;
  }
  .device-icons { position: absolute; left: 46px; top: 261px; display: flex; gap: 12px; align-items: flex-end; }
  .order-button {
    position: absolute; left: 241px; top: 205px; width: 192px; height: 49px; background: var(--gold);
    color: var(--text-light); display: flex; align-items: center; justify-content: center; gap: 12px;
    font-family: "Archivo", Arial, sans-serif; font-size: 11.5px; font-weight: 700; letter-spacing: 1.8px; text-decoration: none;
  }

  .slider-dots { position: absolute; left: 545px; top: 448px; display: flex; gap: 8px; }
  .slider-dots i { display: block; width: 7.5px; height: 7.5px; background: var(--dot); }
  .slider-dots i.active { background: var(--dot-active); }

  .section-title {
    position: absolute; left: 0; width: 1191px; top: 476px; text-align: center;
    font-family: "Archivo", Arial, sans-serif; font-weight: 800; font-size: 18.6px; color: var(--title-ink); letter-spacing: 0.5px;
  }
  .step-num {
    position: absolute; top: 522px; font-family: "Archivo", Arial, sans-serif; font-weight: 700;
    font-size: 44px; line-height: 44px; color: var(--faint-blue);
  }
  .chat-tab {
    position: absolute; left: 1025px; top: 525px; width: 150px; height: 20px; background: var(--chat-bg);
    border-radius: 5px 5px 0 0; color: #ffffff; font-size: 7.3px; line-height: 20px; padding-left: 8px; overflow: hidden;
  }
  .chat-tab::after {
    content: ""; position: absolute; right: -6px; top: -2px; width: 16px; height: 16px; border-radius: 50%; background: var(--green);
  }
  .scrollbar { position: absolute; right: 0; top: 0; width: 9px; height: 545px; background: var(--scroll); }
  .scrollbar::before { content: ""; position: absolute; left: 2px; top: 6px; width: 5px; height: 82px; background: #c1c1c1; border-radius: 2px; }
</style>
</head>
<body>
  <header class="site-header">
    <span class="brand">Trimfit</span>
    <span class="brand-divider"></span>
    <span class="tagline">Get the size you need!</span>
    <div class="contact-box">
      <svg width="8" height="8" viewBox="0 0 24 24" fill="#ffffff"><path d="M6.6 10.8a15 15 0 0 0 6.6 6.6l2.2-2.2a1 1 0 0 1 1-.25 11.4 11.4 0 0 0 3.6.6 1 1 0 0 1 1 1V20a1 1 0 0 1-1 1A17 17 0 0 1 3 4a1 1 0 0 1 1-1h3.5a1 1 0 0 1 1 1c0 1.25.2 2.45.57 3.57a1 1 0 0 1-.25 1z"/></svg>
      <span>Call us (555) 014 2290</span>
      <svg class="hours" width="9" height="9" viewBox="0 0 24 24" fill="none" stroke="#ffffff" stroke-width="2.4"><circle cx="12" cy="12" r="10"/><path d="M12 6v6l3 2"/></svg>
      <span>Mon-Fri 8AM - 4.30PM</span>
    </div>
    <nav class="main-nav">
      <span style="left:692px;font-size:8.5px;top:10px">CAD</span>
      <span class="nav-cta">ORDER NOW</span>
      <span style="left:794px">DESIGN &amp; QUOTE</span>
      <span style="left:867px">SAMPLES</span>
      <span style="left:915px">ABOUT</span>
      <span style="left:953px">CONTACT</span>
      <span style="left:1001px">ARTICLES</span>
      <svg class="nav-icon" style="left:1060px;top:10px" width="10" height="10" viewBox="0 0 24 24" fill="none" stroke="#ffffff" stroke-width="2.4"><circle cx="10" cy="10" r="7"/><path d="M15 15l6 6"/></svg>
      <span style="left:1097px;top:6px;font-size:14px;font-weight:700">?</span>
      <svg class="nav-icon" style="left:1130px" width="13" height="13" viewBox="0 0 24 24" fill="none" stroke="#ffffff" stroke-width="1.8"><circle cx="12" cy="8" r="5"/><path d="M3 22c1-5 5-7 9-7s8 2 9 7z"/></svg>
      <svg class="nav-icon" style="left:1165px" width="14" height="13" viewBox="0 0 24 22" fill="none" stroke="#ffffff" stroke-width="1.8"><path d="M1 2h4l3 12h12l2-8H7"/><circle cx="10" cy="19" r="1.6"/><circle cx="18" cy="19" r="1.6"/></svg>
    </nav>
  </header>

  <section class="title-band">
    <h2>THE FIRST ONLINE CUSTOM CABINET’S MANUFACTURER</h2>
    <p>Order custom cabinets online with instant price calculator. No hidden fees, top quality warranty.</p>
  </section>

  <section class="banner">
    <div class="banner-photo" role="img" aria-label="Photo of a smiling couple holding mugs in a modern kitchen with grey custom cabinets and a dark tiled backsplash"></div>
    <div class="offer-panel">
      <h1 class="offer-title">Order Cabinets, Drawers,<br>Doors Easily Online!</h1>
      <p class="offer-text">Order cabinets, drawers, or doors online and have them shipped directly to your doorstep.</p>
      <p class="device-label">ORDER FROM ANY DEVICE</p>
      <div class="device-icons">
        <svg width="13" height="21" viewBox="0 0 14 22" fill="none" stroke="#e6e6e6" stroke-width="1.1"><rect x="1" y="1" width="12" height="20" rx="2"/><line x1="5" y1="3" x2="9" y2="3"/></svg>
        <svg width="26" height="18" viewBox="0 0 26 18" fill="none" stroke="#e6e6e6" stroke-width="1.1"><rect x="3" y="1" width="20" height="13" rx="1"/><path d="M1 15h24v1.5H1z"/></svg>
        <svg width="23" height="19" viewBox="0 0 24 20" fill="none" stroke="#e6e6e6" stroke-width="1.1"><rect x="1" y="1" width="22" height="13" rx="1"/><line x1="12" y1="14" x2="12" y2="18"/><line x1="7" y1="18.5" x2="17" y2="18.5"/></svg>
      </div>
      <a class="order-button" href="#">ORDER ONLINE
        <svg width="32" height="26" viewBox="0 0 32 26" fill="none" stroke="#ffffff" stroke-width="1.3">
          <rect x="3" y="6" width="26" height="13" rx="6.5"/>
          <text x="16" y="15.5" fill="#ffffff" stroke="none" font-size="7" font-weight="700" text-anchor="middle" font-family="Archivo, Arial, sans-serif">BUY</text>
          <path d="M19 15l3 8 1.5-3 3 1" stroke-linejoin="round"/>
          <path d="M2 2l2 2M6 0v2M0 6h2"/>
        </svg>
      </a>
    </div>
  </section>

  <div class="slider-dots"><i></i><i></i><i></i><i></i><i class="active"></i><i></i><i></i></div>

  <h3 class="section-title">EASY QUOTE &amp; ORDER</h3>
  <span class="step-num" style="left:262px">1</span>
  <span class="step-num" style="left:425px">2</span>
  <span class="step-num" style="left:597px">3</span>
  <span class="step-num" style="left:782px">4</span>

  <div class="chat-tab">Questions? Start chat, we are online!</div>
  <div class="scrollbar"></div>
</body>
</html>
```